Doctors Office Web Design

Name of the business is Lin-Yue Hart M.D.
We need a web design that is attractive for women that want to see Dr. Lin-Yue Hart for Obstetrician Gynecology and Pregnancy care. Dr. Hart earned her degree from Carrow Ridge Medical College of obstetrician gynecology. We want to attract women of child bearing ages to come to our offices for health, education, and pregnancies.

Please visit http://www.drhartclinicweb.com/ to help you get a feel for who we are. We will be adding some pictures and logo in the next few days.

We are looking for to have pages for and tabs including
About Us- History, Our Staff, Dr. Hart
Patient Information- Appointments, E-Prescriptions, Payments Accepted, Insurance
Health- General, Sexual, Mental, Affiliates
Pregnancy- Minimally invasive surgery(our specialty), 4-D Ultra Sound, Hospital Affiliations
Media- News,Pictures, Videos
Locations- Palmer Office, Westvale Office

The colors we would like to use are pastel colors, magenta, and plum

Target Market(s)

Women of all ages with an emphasis on 25-65 year olds

Industry/Entity Type

Business

Requirements
Must have
• Needs to include a location for a our videos and pictures that I will submit shortly. We also want a map to our location or atleast a place for one.
Nice to have
• A place for a google map of our office locations.

```html
<!DOCTYPE html>
<html lang="en">
<head>
<meta charset="utf-8">
<title>Dr. Hart's – Obstetrics &amp; Gynecology</title>
<link href="https://fonts.googleapis.com/css2?family=Tinos:ital,wght@0,400;0,700;1,400&display=swap" rel="stylesheet">
<style>
  :root {
    --pink-bg: #f7b4d9;
    --pink-light: #fbc7e4;
    --magenta: #e24fcf;
    --purple: #9b22c9;
    --lavender: #a48fe2;
    --orchid: #c650d6;
    --orchid-soft: #c86ad8;
    --orchid-pale: #d486e0;
    --tab-text: #f6dcf6;
    --ink: #111111;
    --white: #ffffff;
  }
  * { margin: 0; padding: 0; box-sizing: border-box; }
  html, body { width: 1200px; height: 900px; overflow: hidden; }
  body {
    position: relative;
    font-family: "Tinos", "Times New Roman", serif;
    color: var(--ink);
    background: linear-gradient(160deg, var(--pink-light) 0%, var(--pink-bg) 55%, #f5a9d3 100%);
  }
  .corner-shapes { position: absolute; inset: 0; }

  .side-menu { position: absolute; left: 0; top: 0; width: 92px; list-style: none; }
  .side-menu li {
    height: 46px; display: flex; align-items: center; justify-content: center;
    text-align: center; color: var(--white); font-size: 16px; line-height: 16px;
    letter-spacing: -0.5px; border: 2px solid #e8d8f4;
  }
  .side-menu .is-dark { background: var(--purple); }
  .side-menu .is-light { background: var(--lavender); }

  .office-header { position: absolute; left: 760px; top: 0; width: 380px; text-align: center; }
  .office-header .practice-name { font-size: 54px; font-weight: 700; line-height: 54px; letter-spacing: 1px; }
  .office-header .rule { height: 2px; background: var(--ink); margin: 0 0 4px 0; }
  .offices { display: flex; }
  .office { width: 50%; font-size: 16px; line-height: 20px; letter-spacing: -0.3px; }
  .office + .office { border-left: 2px solid var(--ink); height: 128px; }

  .practice-title {
    position: absolute; left: 100px; top: 236px; width: 1000px; text-align: center;
    font-size: 136px; font-weight: 400; line-height: 150px; color: var(--ink);
  }

  .welcome {
    position: absolute; left: 190px; top: 486px; width: 820px; text-align: center;
    font-size: 32px; line-height: 42px;
  }
  .badge { position: absolute; left: 1024px; top: 500px; width: 104px; height: 160px; background: var(--white); border: 1px solid #ddd; }

  .main-nav { position: absolute; left: 284px; top: 776px; display: flex; gap: 10px; list-style: none; }
  .main-nav li {
    width: 118px; height: 130px; padding-top: 10px; display: flex; align-items: flex-start; justify-content: center;
    text-align: center; color: var(--tab-text); font-size: 27px; line-height: 32px;
    background: var(--orchid-soft); border: 3px solid var(--orchid-pale);
  }
  .main-nav .is-current { background: var(--orchid); align-items: center; padding-top: 0; }

  .footer-mark { position: absolute; bottom: 2px; font-size: 18px; }
  .footer-mark.left { left: 4px; }
  .footer-mark.right { right: 6px; }
</style>
</head>
<body>
  <svg class="corner-shapes" width="1200" height="900" viewBox="0 0 1200 900" aria-hidden="true">
    <polygon points="0,500 300,900 0,900" fill="var(--magenta)"/>
    <polygon points="1200,490 940,900 1200,900" fill="var(--magenta)"/>
  </svg>

  <ul class="side-menu">
    <li class="is-dark">Send to a friend</li>
    <li class="is-light">Maps</li>
    <li class="is-dark">Videos</li>
    <li class="is-light">Photo Gallery</li>
  </ul>

  <header class="office-header">
    <div class="practice-name">DR. HART'S</div>
    <div class="rule"></div>
    <div class="offices">
      <div class="office">2210 Meridian Avenue<br>Suite 210-212<br>Westvale, Florida 33090<br>tel:(555)201-4400<br>Fax:(555)201-4410</div>
      <div class="office">480 N.W 9th Street<br>Suite 204B<br>Palmer, Florida 33092<br>Tel:(555)318-2200<br>Fax:(555)318-2210</div>
    </div>
  </header>

  <div class="practice-title">DR. HART'S</div>

  <p class="welcome">Welcome to Dr. Lin-Yue Hart's website. Here you will be able to find information about both of our offices, meet Dr. Hart and her staff, and browse through our women's health links to learn more about pregnancy, nutrition, exercise, and other women's health issues.</p>

  <div class="badge" role="img" aria-label="Awareness month badge"></div>

  <ul class="main-nav">
    <li class="is-current">Home</li>
    <li>About the Practice</li>
    <li>Meet Dr. Hart</li>
    <li>OB/GY N Info.</li>
    <li>The Pregnancy Page</li>
  </ul>

  <div class="footer-mark left">LIN-YUE HART, M.D., P.A.</div>
  <div class="footer-mark right">LIN-YUE HART, M.D., P.A.</div>
</body>
</html>
```